IT company requires website redesign

I have an old boring website that I want to update - www.tvkb-example.net
I am a growing IT company beginning to look after more healthcare professionals such as medical and dental practices so a more professional look is required

Blue and orange are the company colours. See one of our local competitors for your reference and ideas - https://www.plinth-halvard.example.au

Target Market(s)

Medical, dental, professional, solicitors etc

Industry/Entity Type

It Support

Number of Pages Required

5+ page

Colors

Designer to choose colors to be used in the design.

Requirements
Must have
• Classy feel, simple with the 'less is more' approach
• On support page, links to support items, a couple more to come
• Reference to our technology partners
• Easy to read
Nice to have
• Company colours are blue with a little orange but I willing to consider new web colour schemes
• leave the rest to you

```html
<!DOCTYPE html>
<html lang="en">
<head>
<meta charset="utf-8">
<title>Meridale Systems – IT Support</title>
<link rel="stylesheet" href="https://fonts.googleapis.com/css2?family=Jost:wght@300;400;500;600;700&display=swap">
<style>
:root{
  --navy:#2f3263;
  --navy-deep:#22254b;
  --orange:#e2672a;
  --ink:#2b2b35;
  --muted:#5d6070;
  --line:#dcdde3;
  --paper:#ffffff;
  --soft:#f6f6f8;
}
*{box-sizing:border-box;margin:0;padding:0}
html,body{width:1200px;height:3557px;overflow:hidden}
body{font-family:"Jost",sans-serif;color:var(--ink);background:var(--paper);position:relative}
.abs{position:absolute}
a{color:inherit;text-decoration:none}

/* header */
.topbar{top:0;left:0;width:1200px;height:83px;background:var(--paper)}
.social{display:flex;gap:8px;left:95px;top:31px}
.social span{width:18px;height:18px;border-radius:50%;background:var(--ink);display:block}
.brand{left:0;width:1200px;top:20px;text-align:center;font-weight:600;font-size:24px;color:var(--navy);letter-spacing:.5px}
.brand i{display:inline-block;width:12px;height:12px;border-radius:50%;background:var(--orange);margin-right:8px;vertical-align:2px}
.contact-top{right:95px;top:30px;display:flex;gap:22px;font-size:13px;color:var(--ink)}
.contact-top svg{vertical-align:-3px;margin-right:6px}
.nav{top:83px;left:0;width:1200px;height:36px;border-top:1px solid var(--line);border-bottom:1px solid var(--line)}
.nav a{position:absolute;top:8px;font-size:13px;color:var(--ink)}
.nav a.active{color:var(--navy);font-weight:500}
.nav a.active::before{content:"";position:absolute;left:-18px;right:-18px;top:-9px;height:2px;background:var(--navy)}

/* hero */
.hero{top:119px;left:0;width:1200px;height:517px;background:linear-gradient(135deg,#8a7d72 0%,#6e6660 40%,#9a928a 70%,#5d5650 100%)}
.hero::after{content:"";position:absolute;inset:0;background:rgba(30,28,40,.42)}
.hero-copy{position:absolute;z-index:2;left:0;width:1200px;text-align:center;color:#fff}
.hero h1{font-weight:500;line-height:1.05}
.hero h1 .small{display:block;font-size:46px}
.hero h1 .big{display:block;font-size:64px}
.hero p{font-size:22px;margin-top:14px}
.btn{display:inline-block;font-size:13px;font-weight:500;padding:0;height:38px;line-height:36px;width:120px;text-align:center;border:1px solid #fff;color:#fff}
.btn.fill{background:var(--orange);border-color:var(--orange)}
.btn.dark{border-color:var(--navy);color:var(--navy)}
.hero-btns{margin-top:26px;display:flex;gap:14px;justify-content:center}
.tabs{z-index:2;top:406px;left:119px;width:962px;display:flex;gap:18px}
.tabs div{flex:1;color:#fff;font-size:18px;font-weight:500;padding-bottom:10px;border-bottom:2px solid rgba(255,255,255,.85)}

.about{top:636px;left:0;width:1200px;height:657px;background:var(--navy)}
.cards{top:598px;left:95px;width:1012px;height:166px;background:#fff;display:flex;box-shadow:0 4px 14px rgba(0,0,0,.18);z-index:3}
.cards .card{flex:1;padding:22px 46px;border-right:1px solid var(--line);font-size:11.5px;line-height:1.55;color:var(--muted)}
.cards .card:last-child{border-right:0}
.cards svg{display:block;margin-bottom:14px}

/* about */
.sec-title{font-size:36px;font-weight:400;color:#fff}
.sec-title b{font-weight:700}
.photo{background:linear-gradient(135deg,#c9c6c2,#8c8a92)}
.about-text{left:628px;top:922px;width:465px;color:#fff;font-size:12px;line-height:1.6}
.about-text h3{font-size:20px;font-weight:500;margin-bottom:12px}
.about-text h4{font-size:14px;font-weight:500;text-decoration:underline;margin:10px 0 6px}
.about-text p{margin-bottom:6px;color:#e3e4ef}

/* services */
.services{top:1293px;left:0;width:1200px;height:574px;background:var(--soft)}
.offer{top:1423px;left:95px;width:232px;height:344px;background:#fff;border:1px solid var(--line);padding:64px 20px 0 22px}
.offer h3{font-size:20px;font-weight:500;color:var(--ink);position:relative;margin-bottom:12px}
.offer h3::before{content:"";position:absolute;left:-22px;top:-6px;width:3px;height:36px;background:var(--navy)}
.offer p{font-size:11.5px;line-height:1.6;color:var(--muted)}
.offer a{display:block;margin-top:22px;font-size:12.5px;font-weight:500;color:var(--navy)}
.svc{width:350px;height:130px;padding:10px 0 0 70px}
.svc svg{position:absolute;left:0;top:12px}
.svc h4{font-size:15px;font-weight:600;color:var(--ink);padding-bottom:6px;margin-bottom:10px;position:relative}
.svc h4::after{content:"";position:absolute;left:0;bottom:0;width:90px;height:1px;background:var(--navy)}
.svc p{font-size:11.5px;line-height:1.6;color:var(--muted);width:250px}
.svc-line{background:var(--line)}

/* testimonial */
.quotes{top:1867px;left:0;width:1200px;height:517px;background:linear-gradient(180deg,#2f3263,#34386c)}
.quote-body{left:140px;width:920px;text-align:center;color:#fff}
.quote-date{font-size:13px;margin-bottom:10px}
.quote-text{font-size:11.5px;line-height:1.6;color:#e3e4ef}
.quote-name{font-size:12px;font-weight:600;margin-top:10px;line-height:1.4}
.quote-role{font-size:11px;color:#d5d6e4;line-height:1.4}
.avatar{left:559px;top:2000px;width:82px;height:82px;border-radius:50%;background:#c8c2bc;border:3px solid #fff}
.qmark{left:588px;top:2068px;width:24px;height:24px;border-radius:50%;background:#fff;color:var(--navy);font-size:22px;line-height:30px;text-align:center;font-weight:700}
.arrow-c{width:24px;height:24px;border-radius:50%;border:1px solid rgba(255,255,255,.6)}
.dots{left:588px;top:2268px;display:flex;gap:6px}
.dots span{width:9px;height:9px;border-radius:50%;background:#fff;opacity:.5}
.dots span:first-child{opacity:1}

.cta{top:2313px;left:95px;width:1012px;height:218px;background:#fff;box-shadow:0 4px 16px rgba(0,0,0,.15);text-align:center;padding-top:44px}
.cta p{font-size:27px;line-height:1.35;color:var(--ink)}
.cta .btn{margin-top:22px}

/* team */
.team-title{top:2588px;left:0;width:1200px;text-align:center;font-size:36px;color:var(--navy);font-weight:400}
.team-title b{font-weight:700;color:var(--ink)}
.member{top:2664px;width:240px;height:251px}
.member.feature{border:6px solid #fff;z-index:2;box-shadow:0 4px 12px rgba(0,0,0,.2)}
.plate{left:0;bottom:0;width:100%;height:56px;background:var(--navy);color:#fff;text-align:center;padding-top:8px}
.plate b{display:block;font-size:16px;font-weight:500}
.plate small{font-size:11px}

/* partners */
.footer{top:3115px;left:0;width:1200px;height:391px;background:var(--navy)}
.partners{top:2984px;left:95px;width:1012px;height:183px;background:#fff;box-shadow:0 4px 16px rgba(0,0,0,.15);z-index:3}
.badge{top:62px;height:56px}

.fcol{top:3226px;color:#fff;font-size:12px;line-height:1.6}
.fcol h5{font-size:19px;font-weight:600;margin-bottom:14px;padding-bottom:6px;position:relative}
.fcol h5::after{content:"";position:absolute;left:0;bottom:0;width:36px;height:1px;background:#fff}
.fcol.right h5::after{left:auto;right:0}
.fcol li{list-style:none;margin-bottom:10px}
.fbrand{font-size:20px;font-weight:600;color:#fff;margin-bottom:16px}
.copy{top:3506px;left:0;width:1200px;height:51px;background:var(--navy-deep);color:#c7c9da;font-size:11px;text-align:center;line-height:51px}
</style>
</head>
<body>

<header class="abs topbar">
  <div class="abs social" aria-label="Social links"><span></span><span></span><span></span><span></span></div>
  <div class="abs brand"><i></i>Meridale Systems</div>
  <div class="abs contact-top">
    <span><svg width="14" height="14" viewBox="0 0 24 24"><path d="M6.6 10.8a15 15 0 0 0 6.6 6.6l2.2-2.2a1 1 0 0 1 1-.25 11 11 0 0 0 3.6.6 1 1 0 0 1 1 1V20a1 1 0 0 1-1 1A17 17 0 0 1 3 4a1 1 0 0 1 1-1h3.5a1 1 0 0 1 1 1 11 11 0 0 0 .6 3.6 1 1 0 0 1-.25 1z" fill="#2b2b35"/></svg>Ph: 1300-000 417</span>
    <span><svg width="15" height="12" viewBox="0 0 24 18"><rect x="1" y="1" width="22" height="16" rx="2" fill="none" stroke="#2b2b35" stroke-width="2"/><path d="M1 2l11 8 11-8" fill="none" stroke="#2b2b35" stroke-width="2"/></svg>Email: info@tvkb-example.net</span>
  </div>
</header>

<nav class="abs nav">
  <a class="active" style="left:249px">Home</a>
  <a style="left:360px">Our Services</a>
  <a style="left:508px">About Us</a>
  <a style="left:637px">Our Team</a>
  <a style="left:771px">Contact Us</a>
  <a style="left:909px">Support</a>
</nav>

<section class="abs hero" role="img" aria-label="Overhead photo of a team working at a desk with laptop and printed charts">
  <div class="hero-copy" style="top:98px">
    <h1><span class="small">Welcome to</span><span class="big">Meridale Systems</span></h1>
    <p>A Better Tomorrow, Through Intelligent use of Technology Today!</p>
    <div class="hero-btns"><a class="btn fill">Contact Us</a><a class="btn">Know More</a></div>
  </div>
  <div class="abs tabs"><div>Software</div><div>Products</div><div>Solutions</div></div>
</section>

<section class="abs about">
  <h2 class="abs sec-title" style="top:188px;left:0;width:1200px;text-align:center"><b>Know</b> About Us</h2>
</section>

<div class="abs cards">
  <div class="card">
    <svg width="40" height="40" viewBox="0 0 40 40" fill="none" stroke="#2f3263" stroke-width="2"><circle cx="20" cy="20" r="7"/><path d="M20 4v6M20 30v6M4 20h6M30 20h6M8.7 8.7l4.2 4.2M27.1 27.1l4.2 4.2M8.7 31.3l4.2-4.2M27.1 12.9l4.2-4.2"/></svg>
    Meridale Systems has the tools, capabilities and expertise to guide any organisation with their software requirements
  </div>
  <div class="card">
    <svg width="40" height="40" viewBox="0 0 40 40" fill="none" stroke="#2f3263" stroke-width="2"><path d="M6 24c4-2 8-2 12 2l6-6c2-2 6-2 8 0l2 2M4 30h10l8 4 14-8"/><rect x="14" y="6" width="12" height="10"/></svg>
    We will determine and provide appropriate products and services to address your technology requirements
  </div>
  <div class="card">
    <svg width="40" height="40" viewBox="0 0 40 40" fill="none" stroke="#2f3263" stroke-width="2"><path d="M10 30c-2-6 2-14 10-18l10-6-4 12c-3 8-10 12-16 12z"/><circle cx="22" cy="16" r="3"/><path d="M6 34l6-6"/></svg>
    A full range of IT Solutions, includes carefully selected IT Service Partners to minimize risk and improve continuity
  </div>
</div>

<div class="abs photo" style="left:95px;top:920px;width:235px;height:140px" role="img" aria-label="Photo of a smiling man at his office computer"></div>
<div class="abs photo" style="left:340px;top:920px;width:230px;height:140px;background:linear-gradient(135deg,#d8d2c8,#9a8f84)" role="img" aria-label="Photo of a small team gathered in an office"></div>
<div class="abs photo" style="left:95px;top:1070px;width:235px;height:140px;background:linear-gradient(135deg,#e6e6e6,#7f8088)" role="img" aria-label="Photo of colleagues in a meeting at a white table"></div>
<div class="abs photo" style="left:340px;top:1070px;width:230px;height:140px;background:linear-gradient(135deg,#eceae6,#b7ada2)" role="img" aria-label="Photo of a smiling support staff member"></div>

<div class="abs about-text">
  <h3>Welcome to our website</h3>
  <p>Welcome to Meridale Systems where we believe that a better tomorrow, starts through intelligent use of technology today!</p>
  <p>Meridale Systems is a valued added Information technology company supplying and implementing hardware and software that are complemented by the provision of associated support services and solutions.</p>
  <h4>Experience &amp; Knowledge</h4>
  <p>Collectively Meridale Systems has over 100+ Years of experience &amp; knowledge as well as a skill base across all touch points of IT and Business.</p>
  <a class="btn" style="margin-top:14px">Know More</a>
</div>

<section class="abs services">
  <h2 class="abs" style="left:104px;top:60px;font-size:36px;font-weight:400;color:var(--navy)"><b style="color:var(--ink)">Our</b> Services</h2>
</section>

<div class="abs offer">
  <h3>What We Offer</h3>
  <p>Permanent Broadband Connections, Network Raid, Network Integration, Networked laser Copiers, Consultancy, Supply all types of PC's, Switches and Hubs, Laptops, POS Hardware, Related Cabling Capabilities</p>
  <a>Know More . . .</a>
</div>

<div class="abs svc-line" style="left:375px;top:1540px;width:730px;height:1px"></div>
<div class="abs svc-line" style="left:375px;top:1670px;width:730px;height:1px"></div>
<div class="abs svc-line" style="left:725px;top:1425px;width:1px;height:370px"></div>

<div class="abs svc" style="left:375px;top:1418px">
  <svg width="50" height="50" viewBox="0 0 50 50" fill="none" stroke="#2f3263" stroke-width="2"><rect x="8" y="10" width="34" height="24"/><path d="M18 42h14M25 34v8"/><circle cx="25" cy="22" r="5"/></svg>
  <h4>Software</h4><p>Meridale Systems has the tools, capabilities and expertise to guide any organisation with their software requirements</p>
</div>
<div class="abs svc" style="left:760px;top:1418px">
  <svg width="50" height="50" viewBox="0 0 50 50" fill="none" stroke="#2f3263" stroke-width="2"><rect x="6" y="8" width="20" height="14"/><rect x="30" y="16" width="14" height="26"/><path d="M6 30h20v12H6z"/></svg>
  <h4>Products</h4><p>We will determine and provide appropriate products and services to address your technology requirements</p>
</div>
<div class="abs svc" style="left:375px;top:1550px">
  <svg width="50" height="50" viewBox="0 0 50 50" fill="none" stroke="#2f3263" stroke-width="2"><circle cx="25" cy="25" r="8"/><path d="M25 6v8M25 36v8M6 25h8M36 25h8M12 12l5 5M33 33l5 5M12 38l5-5M33 17l5-5"/></svg>
  <h4>Solutions</h4><p>A full range of IT Solutions, includes carefully selected IT Service Partners to minimize risk and improve continuity</p>
</div>
<div class="abs svc" style="left:760px;top:1550px">
  <svg width="50" height="50" viewBox="0 0 50 50" fill="none" stroke="#2f3263" stroke-width="2"><rect x="6" y="12" width="38" height="24"/><path d="M28 18c-4-2-8 0-6 3s6 2 6 5-4 4-7 2M25 15v20"/></svg>
  <h4>Finance – Flexi Rent</h4><p>Concerned about your budget? We can help you with payment plan options.</p>
</div>
<div class="abs svc" style="left:375px;top:1682px">
  <svg width="50" height="50" viewBox="0 0 50 50" fill="none" stroke="#2f3263" stroke-width="2"><path d="M25 5l18 10v20L25 45 7 35V15z"/><path d="M19 22l-4 4 4 4M31 22l4 4-4 4"/></svg>
  <h4>Programming</h4><p>Electronic design manufacturing and microprocessor programming</p>
</div>
<div class="abs svc" style="left:760px;top:1682px">
  <svg width="50" height="50" viewBox="0 0 50 50" fill="none" stroke="#2f3263" stroke-width="2"><rect x="8" y="18" width="34" height="18"/><path d="M14 18V8h22v10M14 30v12h22V30"/></svg>
  <h4>Copiers</h4><p>B&amp;W Photocopiers &amp; RIP with full integration into networks for printing and scanning</p>
</div>
<a class="abs" style="left:1020px;top:1786px;font-size:13px;font-weight:500;color:var(--ink)">View More . . .</a>

<section class="abs quotes">
  <h2 class="abs sec-title" style="top:62px;left:0;width:1200px;text-align:center"><b>What</b> Peoples Say !</h2>
  <div class="abs arrow-c" style="left:47px;top:290px"></div>
  <div class="abs arrow-c" style="left:1128px;top:290px"></div>
</section>
<div class="abs avatar" role="img" aria-label="Client portrait"></div>
<div class="abs qmark">“</div>
<div class="abs quote-body" style="top:2102px">
  <div class="quote-date">24 April 2015</div>
  <p class="quote-text">Meridale Systems have been our IT support company for over 10 years. So why do we stick with them? Because they are awesome!! Tom and his staff are consistently able to solve our many and varied problems. Whether we phone about server functionality, email capacity, software issues or IT security, Tom and the team are always able to provide a quick and efficient response, leaving us to get on with our business. Reliable, knowledgeable, cost effective – Meridale Systems are an asset to our company and I cannot recommend them highly enough.</p>
  <div class="quote-name">Renata Ellison</div>
  <div class="quote-role">Administration Manager</div>
</div>
<div class="abs dots"><span></span><span></span></div>

<div class="abs cta">
  <p>A Better Tomorrow, through intelligent use of Technology Today!<br>Contact our team today!</p>
  <a class="btn dark">Know More</a>
</div>

<h2 class="abs team-title"><b>Meet Our</b> Team Members</h2>
<div class="abs member" style="left:0;background:linear-gradient(135deg,#7a6a5c,#3e3834)" role="img" aria-label="Team member portrait"></div>
<div class="abs member" style="left:240px;background:linear-gradient(135deg,#5c554e,#1f1d1c)" role="img" aria-label="Team member portrait"></div>
<div class="abs member" style="left:720px;background:linear-gradient(135deg,#6a4c40,#2a2320)" role="img" aria-label="Team member portrait"></div>
<div class="abs member" style="left:960px;background:linear-gradient(135deg,#8a3c28,#2e2420)" role="img" aria-label="Team member portrait"></div>
<div class="abs member feature" style="left:480px;top:2658px;height:257px;background:linear-gradient(180deg,#e6e6e8,#b8bcc6)" role="img" aria-label="Portrait of head of technical services">
  <div class="abs plate"><b>Tom Hartley</b><small>Head of Technical Services</small></div>
</div>

<section class="abs footer"></section>
<div class="abs partners" aria-label="Technology partners">
  <svg class="abs" style="left:12px;top:82px" width="20" height="20" viewBox="0 0 20 20"><path d="M13 3l-7 7 7 7" fill="none" stroke="#9a9ca8" stroke-width="1.6"/></svg>
  <div class="abs badge" style="left:55px;width:165px;background:#3a7fd0"></div>
  <div class="abs badge" style="left:277px;width:96px;background:#1f4f9a;border-radius:8px"></div>
  <div class="abs badge" style="left:422px;width:183px;top:72px;height:36px;background:#d42a26"></div>
  <div class="abs badge" style="left:655px;width:110px;top:66px;height:48px;background:#e6e6e8;border-radius:6px"></div>
  <div class="abs badge" style="left:810px;width:150px;background:#2b8ad8"></div>
  <svg class="abs" style="left:980px;top:82px" width="20" height="20" viewBox="0 0 20 20"><path d="M7 3l7 7-7 7" fill="none" stroke="#9a9ca8" stroke-width="1.6"/></svg>
</div>

<div class="abs fcol" style="left:112px;width:230px">
  <div class="fbrand">Meridale Systems</div>
  <p>Commenced trading in 1996, the retail division was sold in 2002. That September Meridale Systems was launched</p>
</div>
<div class="abs fcol" style="left:441px">
  <h5>Site Map</h5>
  <ul><li>Home</li><li>Our Services</li><li>About Us</li><li>Our Team</li><li>Contact Us</li><li>Support</li></ul>
</div>
<div class="abs fcol" style="left:617px;width:300px">
  <h5>Services</h5>
  <ul style="float:left;width:125px"><li>Software</li><li>Products</li><li>Solutions</li><li>Finance – Flexi Rent</li></ul>
  <ul style="float:left"><li>Programming</li><li>Copiers</li><li>Web Hosting and Design</li></ul>
</div>
<div class="abs fcol right" style="left:900px;width:188px;text-align:right">
  <h5>Contact Us</h5>
  <div style="font-size:13px;font-weight:500">Call Us</div>
  <div style="font-size:22px;font-weight:600;line-height:1.2">1300-000 417</div>
  <div style="margin-top:4px">Email: <b>info@tvkb-example.net</b></div>
  <div style="display:flex;gap:7px;justify-content:flex-end;margin-top:8px" aria-label="Social links">
    <span style="width:18px;height:18px;border-radius:50%;background:#fff"></span>
    <span style="width:18px;height:18px;border-radius:50%;background:#fff"></span>
    <span style="width:18px;height:18px;border-radius:50%;background:#fff"></span>
    <span style="width:18px;height:18px;border-radius:50%;background:#fff"></span>
  </div>
</div>

<div class="abs copy">© 2019 Meridale Systems | All rights reserved</div>

</body>
</html>
```